New image for luxury travel blog

I would like to refresh my blog and social media platforms and would require a new design concept for lilyfarwander.net. I will require the following:

- Top banner for website using current size
- Similar imagery for Facebook Page, Twitter Profile, Google Plus (page and personal profile)
- New profile photo (for each social platform) in appropriate sizes for each platform (with white round shape as I currently have), and 2-3 larger options (500x500, 250x250px)
- Artwork for business card (pavex.net)
- A square logo (based on image defined) for Lily Far Wander Notes (that can be used as an ad of just when I need a logo of the blog)
- Copy to use - Lily Far Wander Notes - a luxury travel blog by Beth Kowal Trenholm.
- Current tagline 'Pack light. Meet kin. Wear heels.' should also be used, but suggestions welcome.
- I am partial to a shade of blue

Feel free to use any photo you can find on my blog at http://lilyfarwander.net which you may find appropriate.

```html
<!DOCTYPE html>
<html lang="en">
<head>
<meta charset="utf-8">
<title>Lily Far Wander Notes – Header Banner</title>
<link rel="stylesheet" href="https://fonts.googleapis.com/css2?family=Cutive+Mono&display=swap">
<style>
  :root {
    --sky-top: #3fdbe6;
    --sky-mid: #37d3df;
    --hill-light: #2fc3cf;
    --hill-dark: #1b97a6;
    --ink: #ffffff;
    --rule: rgba(255, 255, 255, 0.9);
    --portrait-ring: #e6f7f9;
    --portrait-warm: #b77a60;
    --portrait-shade: #5a3a36;
  }

  html, body {
    margin: 0;
    padding: 0;
    width: 1200px;
    height: 104px;
    overflow: hidden;
    background: var(--sky-top);
  }

  .banner {
    position: relative;
    width: 1200px;
    height: 104px;
    overflow: hidden;
    background: linear-gradient(to bottom, var(--sky-top) 0%, var(--sky-mid) 60%, var(--hill-light) 100%);
    font-family: "Cutive Mono", "Courier New", monospace;
    color: var(--ink);
  }

  .banner__landscape {
    position: absolute;
    left: 0;
    bottom: 0;
    width: 1200px;
    height: 62px;
    display: block;
  }

  .banner__title {
    position: absolute;
    left: 0;
    width: 994px;
    top: 10px;
    margin: 0;
    text-align: center;
    font-size: 21px;
    font-weight: 400;
    letter-spacing: 19px;
    line-height: 28px;
    text-indent: 19px;
    white-space: nowrap;
  }

  .banner__rule {
    position: absolute;
    left: 140px;
    top: 47px;
    width: 714px;
    height: 1px;
    background: var(--rule);
  }

  .banner__subtitle {
    position: absolute;
    left: 0;
    width: 994px;
    top: 56px;
    margin: 0;
    text-align: center;
    font-size: 15px;
    letter-spacing: 4.6px;
    line-height: 20px;
    white-space: nowrap;
  }

  .banner__portrait {
    position: absolute;
    left: 1048px;
    top: -2px;
    width: 90px;
    height: 90px;
    border-radius: 50%;
    box-sizing: border-box;
    border: 3px solid var(--portrait-ring);
    background: radial-gradient(circle at 55% 45%, var(--portrait-warm) 0%, #9a5f4c 45%, var(--portrait-shade) 100%);
  }
</style>
</head>
<body>
  <header class="banner">
    <svg class="banner__landscape" viewBox="0 0 1200 62" preserveAspectRatio="none" role="img" aria-label="Soft photo of forested rolling hills washed in turquoise">
      <defs>
        <linearGradient id="hillFade" x1="0" y1="0" x2="0" y2="1">
          <stop offset="0" stop-color="var(--hill-light)" stop-opacity="0.6"/>
          <stop offset="1" stop-color="var(--hill-dark)"/>
        </linearGradient>
      </defs>
      <path d="M0 22 C120 12 240 14 360 20 C480 26 560 10 700 14 C840 18 960 8 1080 16 C1140 20 1180 18 1200 16 L1200 62 L0 62 Z" fill="url(#hillFade)"/>
    </svg>

    <h1 class="banner__title">LILY FAR WANDER NOTES</h1>
    <div class="banner__rule"></div>
    <p class="banner__subtitle">A luxury travel blog by Beth Kowal Trenholm.</p>

    <div class="banner__portrait" role="img" aria-label="Round portrait photo of the blog author"></div>
  </header>
</body>
</html>
```